Marlowe Holdings LLC - Business Cards

Need the following information on the cards:

Name: Dean R Vossler
Title: Chief Executive Manager

Business address:
412 N Ridgeview Lane #118
Elm Harbor, Il 60412

Phone: (555) 555-0148 - Business
KPV FFL license number: 5-21-xxx-xx-xx-04519
Email: dean.vossler@marloweholdingsffl.com

Target Market(s)

Firearm owners

Industry/Entity Type

Firearms industry,

Contact Information for Business Card

Contact number, name and title, web page address, email, business address and kpv license number,

Requirements
Must have
• Name, title, business address, phone numbers, KPV license numbers, web page address and email address.
Nice to have
• Cellphone number,

```html
<!DOCTYPE html>
<html lang="en">
<head>
<meta charset="utf-8">
<title>Marlowe Holdings LLC – Business Cards</title>
<link rel="stylesheet" href="https://fonts.googleapis.com/css2?family=Carlito:wght@400;700&display=swap">
<style>
  :root {
    --bg: #dcdedd;
    --card-red: #cf2024;
    --card-white: #ffffff;
    --ink-dark: #2a2a2a;
  }
  * { box-sizing: border-box; margin: 0; padding: 0; }
  html, body { width: 1200px; height: 1200px; overflow: hidden; }
  body {
    background: var(--bg);
    font-family: "Carlito", "Calibri", sans-serif;
    position: relative;
  }
  .card {
    position: absolute;
    left: 307px;
    width: 540px;
    height: 312px;
    border-radius: 17px;
    overflow: hidden;
  }
  .card-front { top: 188px; background: var(--card-white); }
  .card-back { top: 653px; background: var(--card-red); color: var(--card-white); }

  .front-band {
    position: absolute; left: 0; right: 0; bottom: 0; height: 30px;
    background: var(--card-red);
  }
  .brand-mark {
    position: absolute;
    display: flex; align-items: center; justify-content: center;
    border-radius: 50%;
    text-align: center;
    font-weight: 700;
    text-transform: uppercase;
    line-height: 1.1;
  }
  .card-front .brand-mark {
    left: 192px; top: 80px; width: 156px; height: 156px;
    border: 1.5px solid var(--ink-dark);
    color: var(--card-red);
    font-size: 20px;
    letter-spacing: 1px;
  }
  .card-back .brand-mark {
    left: 403px; top: 27px; width: 106px; height: 106px;
    border: 1.5px solid var(--card-white);
    color: var(--card-white);
    font-size: 14px;
    letter-spacing: 0.8px;
  }

  .icon {
    position: absolute; left: 30px;
    width: 18px; height: 18px;
    background: var(--card-white);
    border-radius: 4px;
  }
  .icon svg { display: block; width: 18px; height: 18px; }
  .icon-pin { height: 27px; border-radius: 4px 4px 0 0; }

  .holder-name {
    position: absolute; left: 57px; top: 37px;
    font-size: 20px; line-height: 1;
    white-space: nowrap;
  }
  .holder-name strong { font-weight: 700; }
  .holder-name span { font-weight: 400; letter-spacing: 0.3px; }
  .name-rule {
    position: absolute; left: 57px; top: 63px;
    width: 121px; height: 1px; background: var(--card-white);
  }
  .name-rule::before {
    content: ""; position: absolute; left: 0; top: -1px;
    width: 34px; height: 3px; background: var(--card-white);
  }
  .holder-title {
    position: absolute; left: 57px; top: 71px;
    font-size: 12px; white-space: nowrap;
  }
  .contact {
    position: absolute; left: 58px;
    font-size: 14px; white-space: nowrap; line-height: 18px;
  }
  .license-rule {
    position: absolute; left: 0; right: 0; top: 260px;
    height: 1px; background: var(--card-white);
  }
  .license {
    position: absolute; left: 0; right: 0; top: 269px;
    text-align: center; font-weight: 700; font-size: 14px;
  }
</style>
</head>
<body>

<section class="card card-front" aria-label="Card front">
  <div class="brand-mark">Marlowe<br>Holdings<br>LLC</div>
  <div class="front-band"></div>
</section>

<section class="card card-back" aria-label="Card back">
  <div class="icon" style="top:40px">
    <svg viewBox="0 0 18 18"><circle cx="9" cy="6.5" r="2.8" fill="#cf2024"/><rect x="4.5" y="10" width="9" height="5" rx="1.5" fill="#cf2024"/></svg>
  </div>
  <div class="holder-name"><strong>Dean</strong> <span>R Vossler</span></div>
  <div class="name-rule"></div>
  <div class="holder-title">Chief Executive Manager</div>

  <div class="icon" style="top:140px">
    <svg viewBox="0 0 18 18"><path d="M5 4.5c1-.8 1.8-.6 2.3.5l.6 1.4c.2.6 0 1-.5 1.4l-.4.3c.5 1.3 1.4 2.3 2.6 2.9l.4-.4c.4-.5.9-.6 1.4-.3l1.3.7c1 .6 1.1 1.3.3 2.2-1 1.1-2.5 1.1-4 .2C6.8 12 5.3 10 4.6 7.9 4.2 6.6 4.3 5.3 5 4.5z" fill="none" stroke="#cf2024" stroke-width="1.2"/></svg>
  </div>
  <div class="contact" style="top:140px">(555) 555-0148</div>

  <div class="icon" style="top:171px">
    <svg viewBox="0 0 18 18"><rect x="3.5" y="5.5" width="11" height="7.5" fill="none" stroke="#cf2024" stroke-width="1.2"/><path d="M3.5 5.5 9 10l5.5-4.5M3.5 13 7.5 9M14.5 13l-4-4" fill="none" stroke="#cf2024" stroke-width="1.1"/></svg>
  </div>
  <div class="contact" style="top:171px; left:60px">dean.vossler@marloweholdingsffl.com</div>

  <div class="icon" style="top:202px">
    <svg viewBox="0 0 18 18"><g fill="none" stroke="#cf2024" stroke-width="1.1"><circle cx="9" cy="9" r="5.5"/><ellipse cx="9" cy="9" rx="2.4" ry="5.5"/><path d="M3.5 9h11M4.5 6h9M4.5 12h9"/></g></svg>
  </div>
  <div class="contact" style="top:202px; left:60px">marloweholdingsffl.com</div>

  <div class="icon icon-pin" style="top:233px">
    <svg viewBox="0 0 18 18"><path d="M9 13s-3.5-3.6-3.5-6a3.5 3.5 0 0 1 7 0c0 2.4-3.5 6-3.5 6z" fill="none" stroke="#cf2024" stroke-width="1.2"/><circle cx="9" cy="7" r="1.2" fill="#cf2024"/><path d="M4 15.5h10" stroke="#cf2024" stroke-width="1.1"/></svg>
  </div>
  <div class="contact" style="top:233px; left:58px">412 N Ridgeview Lane #118 Elm Harbor, Il 60412</div>

  <div class="license-rule"></div>
  <div class="license">KPV FFL license number: 5-21-xxx-xx-xx-04519</div>

  <div class="brand-mark">Marlowe<br>Holdings<br>LLC</div>
</section>

</body>
</html>
```